Harlow Chiropractic Business card

Health related business card, picture on front, logo on back with a spot to schedule multiple appointments.
address, website, email, name of the clinic, chiropractic physician, www.HarlowChiropractic.example P) 615-482-9153 F)615-482-7361, Drpaulharlow@mailbox.example, 418 Bramwell lane Suite 206., Nashville, TN 37298. I would like for it to be professional, with a slight fun and healthy attitude

Industry/Entity Type

Health Care

Contact Information for Business Card

Health related business card, picture on front, logo on back with appointment times.
address, website, email, name of the clinic, chiropractic physician, www.HarlowChiropractic.example P) 615-482-9153 F)615-482-7361, Drpaulharlow@mailbox.example, 418 Bramwell lane Suite 206., Nashville, TN 37298

Font styles to use
Sans Serif

Colors
3176b5
33b8a4
0255a3
00a990
feeeee

Requirements
Must have
• Dr. Paul Harlow, or Paul Harlow, D.C., I want rounded corners, picture on front

```html
<!DOCTYPE html>
<html lang="en">
<head>
<meta charset="utf-8">
<title>Harlow Chiropractic Business Card</title>
<link rel="stylesheet" href="https://fonts.googleapis.com/css2?family=Cinzel:wght@600&family=Montserrat:wght@400&family=Open+Sans:ital,wght@0,400;1,400&display=swap">
<style>
  :root {
    --stage: #3b3b3b;
    --brand-blue: #0b4f9c;
    --brand-green: #8dc63f;
    --card-white: #f7f7f7;
    --back-tint: #e2e9f1;
    --ink-grey: #555b62;
    --rule-grey: #6d7278;
    --photo-light: #e4e7ea;
    --photo-mid: #b9c3cd;
  }
  * { margin: 0; padding: 0; box-sizing: border-box; }
  html, body { width: 1200px; height: 750px; overflow: hidden; }
  body { background: var(--stage); position: relative; font-family: "Montserrat", sans-serif; }

  .card {
    position: absolute; top: 228px; width: 461px; height: 262px;
    border-radius: 14px; overflow: hidden;
  }
  .card--front { left: 124px; background: var(--card-white); }
  .card--back { left: 618px; background: var(--back-tint); }

  .clinic-name {
    position: absolute; display: flex; align-items: center; gap: 8px;
    font-family: "Cinzel", serif; font-weight: 600; color: var(--brand-blue);
    white-space: nowrap;
  }
  .clinic-name__dot { width: 14px; height: 14px; border-radius: 50%; background: var(--brand-green); flex: none; }
  .card--front .clinic-name { left: 20px; top: 40px; font-size: 22px; }
  .card--back .clinic-name { left: 0; right: 0; top: 24px; justify-content: center; font-size: 19px; }

  .portrait {
    position: absolute; right: 0; top: 0; width: 160px; height: 200px;
    background: radial-gradient(ellipse at 50% 35%, var(--photo-mid) 0%, var(--photo-light) 70%, transparent 100%);
  }

  .wave { position: absolute; left: 0; top: 0; width: 461px; height: 262px; }

  .address {
    position: absolute; left: 17px; top: 148px; color: #fff; font-size: 11.5px; line-height: 14px;
  }
  .contact-list { position: absolute; left: 17px; top: 186px; list-style: none; }
  .contact-list li {
    display: flex; align-items: center; gap: 9px; height: 17.6px;
    color: #fff; font-size: 11.5px;
  }
  .contact-list svg { width: 12px; height: 12px; flex: none; }

  .physician { position: absolute; right: 17px; top: 212px; text-align: right; font-family: "Cinzel", serif; }
  .physician__name { color: var(--brand-green); font-size: 16px; letter-spacing: 0.5px; line-height: 20px; }
  .physician__title { color: #fff; font-size: 11.5px; letter-spacing: 0.8px; line-height: 16px; }

  .appointments { position: absolute; left: 0; top: 66px; width: 100%; font-family: "Open Sans", sans-serif; }
  .appointment-row {
    position: relative; height: 42px; font-size: 13px; color: var(--ink-grey);
  }
  .appointment-row span { position: absolute; top: 0; }
  .appointment-row i { position: absolute; top: 16px; height: 1px; background: var(--rule-grey); }
  .lbl-date { left: 30px; } .rule-date { left: 70px; width: 162px; }
  .lbl-time { left: 242px; } .rule-time { left: 281px; width: 89px; }
  .lbl-ampm { left: 375px; }

  .notice {
    position: absolute; left: 0; bottom: 0; width: 100%; height: 28px;
    background: var(--brand-blue); color: #fff; text-align: center;
    font-family: "Open Sans", sans-serif; font-style: italic; font-size: 10.5px; line-height: 28px;
  }
</style>
</head>
<body>

<section class="card card--front">
  <div class="portrait" role="img" aria-label="Portrait photo of Dr. Paul Harlow"></div>

  <svg class="wave" viewBox="0 0 461 262" aria-hidden="true">
    <path d="M0,126 C90,104 200,120 320,166 C385,192 440,188 461,150 L461,160 C440,203 385,212 320,190 C220,150 100,120 0,148 Z" fill="var(--brand-green)"/>
    <path d="M0,150 C100,124 220,154 322,194 C386,216 442,206 461,166 L461,262 L0,262 Z" fill="var(--brand-blue)"/>
  </svg>

  <div class="clinic-name"><span class="clinic-name__dot"></span>Harlow Chiropractic</div>

  <p class="address">418 Bramwell lane, Suite 206<br>Nashville, TN 37298</p>

  <ul class="contact-list">
    <li><svg viewBox="0 0 12 12"><path d="M2.5 1 L4.5 1 L5.3 3.6 L4 4.6 C4.6 6 5.9 7.3 7.4 8 L8.4 6.7 L11 7.5 L11 9.5 C11 10.3 10.3 11 9.5 11 C5 11 1 7 1 2.5 C1 1.7 1.7 1 2.5 1 Z" fill="var(--brand-green)"/></svg>615-482-9153</li>
    <li><svg viewBox="0 0 12 12"><rect x="3" y="1" width="6" height="3" fill="var(--brand-green)"/><rect x="1" y="4.5" width="10" height="4.5" rx="1" fill="var(--brand-green)"/><rect x="3" y="8" width="6" height="3" fill="var(--brand-green)"/></svg>615-482-7361</li>
    <li><svg viewBox="0 0 12 12"><rect x="1" y="2.5" width="10" height="7" fill="var(--brand-green)"/><path d="M1 2.5 L6 6.5 L11 2.5" stroke="var(--brand-blue)" stroke-width="1" fill="none"/></svg>Drpaulharlow@mailbox.example</li>
    <li><svg viewBox="0 0 12 12"><circle cx="6" cy="6" r="5" fill="var(--brand-green)"/><path d="M1 6 H11 M6 1 C3.5 3.5 3.5 8.5 6 11 M6 1 C8.5 3.5 8.5 8.5 6 11" stroke="var(--brand-blue)" stroke-width="0.8" fill="none"/></svg>www.HarlowChiropractic.example</li>
  </ul>

  <div class="physician">
    <p class="physician__name">Paul Harlow, D.C.,</p>
    <p class="physician__title">CHIROPRACTIC PHYSICIAN</p>
  </div>
</section>

<section class="card card--back">
  <div class="clinic-name"><span class="clinic-name__dot"></span>Harlow Chiropractic</div>

  <div class="appointments">
    <div class="appointment-row"><span class="lbl-date">Date</span><i class="rule-date"></i><span class="lbl-time">Time</span><i class="rule-time"></i><span class="lbl-ampm">am/pm</span></div>
    <div class="appointment-row"><span class="lbl-date">Date</span><i class="rule-date"></i><span class="lbl-time">Time</span><i class="rule-time"></i><span class="lbl-ampm">am/pm</span></div>
    <div class="appointment-row"><span class="lbl-date">Date</span><i class="rule-date"></i><span class="lbl-time">Time</span><i class="rule-time"></i><span class="lbl-ampm">am/pm</span></div>
    <div class="appointment-row"><span class="lbl-date">Date</span><i class="rule-date"></i><span class="lbl-time">Time</span><i class="rule-time"></i><span class="lbl-ampm">am/pm</span></div>
  </div>

  <p class="notice">Please give 24 hours notice cancelling your appointment or a fee may be charged</p>
</section>

</body>
</html>
```